vantrel works cybersecurity website design and development

website design and development for a cybersecurity company. we have a logo and would like site to suit logo colors and look
cybersecurity website should be secure and look professional
main example of site we want to use: https://www.morvisquad.example/
site should be usable on tablet and phones

For each design proposal, please could you provide details of what language you'll use to code the website.

Target Market(s)

insurance companies, financial institutions, private SME, Africa and Europe

Coding

Coded - Design and coding required

Number of Pages Required

5+ page

Requirements
Must have
• 9 Pages:
Home
About us
Contacts
Partners
Blog
Services
( consulting, vulnerability assessment, information systems security audit, ISO compliance, Penetration testing, security awareness training, social engineering test, protection against DDoS, procurement )
Resources
Technologies
Careers
Nice to have
• nice to have all services have their own pages.
design based on logo colors and look

please provide what will be use to code the website

```html
<!DOCTYPE html>
<html lang="en">
<head>
<meta charset="utf-8">
<title>Vantrel Works — Cybersecurity</title>
<link rel="stylesheet" href="https://fonts.googleapis.com/css2?family=Poppins:wght@300;400;500;600;700&family=Raleway:wght@400;500;600;700&display=swap">
<style>
:root{
  --blue:#1588d6;
  --blue-dark:#0b5fa3;
  --navy:#0c1626;
  --navy-2:#162235;
  --card:#242f40;
  --ink:#1d2330;
  --muted:#6b7280;
  --line:#d7dbe1;
  --light:#f1f3f6;
  --footer:#242527;
  --white:#ffffff;
}
*{margin:0;padding:0;box-sizing:border-box}
html,body{width:1200px;height:4501px;overflow:hidden}
body{position:relative;background:var(--white);font-family:"Raleway",sans-serif;color:var(--ink)}
.abs{position:absolute}
.brand{font-family:"Poppins",sans-serif;font-weight:600;color:var(--blue-dark);display:flex;align-items:center;gap:10px}
.brand-mark{width:34px;height:34px;border-radius:50%;background:var(--blue)}
/* header */
.site-header{top:0;left:0;width:1200px;height:78px;background:var(--white)}
.site-header .brand{position:absolute;left:119px;top:18px;font-size:26px}
.main-nav{position:absolute;left:538px;top:29px;display:flex;gap:30px;font-family:"Poppins",sans-serif;font-size:15px;color:#333}
.main-nav a{color:inherit;text-decoration:none}
.main-nav .active{font-weight:600;color:#111;border-bottom:2px solid var(--blue);padding-bottom:3px}
/* hero */
.hero-bg{top:78px;left:0}
.hero-eyebrow{left:147px;top:300px;color:#fff;font-family:"Poppins",sans-serif;font-weight:300;font-size:22px}
.hero-title{left:147px;top:342px;color:#fff;font-family:"Poppins",sans-serif;font-weight:600;font-size:44px;line-height:61px}
.hero-title span{font-weight:400}
.btn{display:inline-flex;align-items:center;justify-content:center;border-radius:22px;font-family:"Poppins",sans-serif;font-weight:600;font-size:12px;letter-spacing:.3px;text-transform:uppercase}
.btn-primary{background:var(--blue);color:#fff}
.btn-light{background:#fff;color:#111}
.scroll-mouse{left:590px;top:754px;width:20px;height:30px;border:2px solid #9aa4b0;border-radius:10px}
.scroll-mouse::after{content:"";position:absolute;left:7px;top:6px;width:2px;height:7px;background:#9aa4b0;border-radius:1px}
/* about */
.eyebrow-blue{color:var(--blue);font-family:"Poppins",sans-serif;font-size:20px}
.about-title{left:150px;top:992px;font-family:"Poppins",sans-serif;font-weight:600;font-size:26px;line-height:39px;color:#222;text-transform:uppercase}
.about-text{left:150px;top:1082px;width:450px;font-size:14px;line-height:24px;color:#555}
/* services */
.section-title{font-family:"Poppins",sans-serif;font-size:33px;font-weight:400;text-align:center;width:1200px;left:0;text-transform:uppercase}
.section-title b{font-weight:700}
.title-rule{left:570px;width:60px;height:3px;background:var(--blue)}
.services-intro{left:0;width:1200px;top:1561px;text-align:center;color:#d8dde5;font-size:14px;line-height:23px}
.service-card{width:283px;height:267px}
.service-card svg.shape{position:absolute;left:0;top:0}
.service-icon{position:absolute;left:111px;top:22px}
.service-sep{position:absolute;left:61px;top:106px;width:161px;height:1px;background:linear-gradient(90deg,transparent,#8a97aa,transparent)}
.service-sep::after{content:"";position:absolute;left:78px;top:-2px;width:5px;height:5px;border-radius:50%;background:#fff}
.service-name{position:absolute;left:0;top:128px;width:283px;text-align:center;color:#fff;font-family:"Poppins",sans-serif;font-weight:500;font-size:14px;line-height:21px;text-transform:uppercase}
.service-go{position:absolute;left:124px;top:202px;width:34px;height:34px;border:1.6px solid #fff;border-radius:50%}
.service-go svg{position:absolute;left:9px;top:9px}
/* partners */
.partner{top:2820px;height:46px;display:flex;align-items:center;gap:8px;font-family:"Poppins",sans-serif;font-size:24px;color:#3c4350}
.partner i{display:block;width:28px;height:28px;border-radius:50%;background:var(--blue)}
.partner-featured{left:292px;top:2790px;width:194px;height:102px;background:#fff;box-shadow:0 6px 20px rgba(0,0,0,.12)}
.pager{top:2926px;left:582px;display:flex;gap:6px}
.pager span{width:8px;height:8px;border-radius:50%;background:#c9ced6}
.pager span.on{background:var(--blue)}
/* blog */
.blog-card{top:3082px;width:277px;height:339px;background:#fff;border:1px solid #e3e6ea}
.blog-card.raised{box-shadow:0 10px 24px rgba(0,0,0,.14)}
.blog-media{position:absolute;left:0;top:0;width:100%;height:152px}
.blog-more{position:absolute;right:0;top:119px;width:33px;height:33px;background:var(--blue)}
.blog-more svg{position:absolute;left:9px;top:9px}
.blog-date{position:absolute;left:22px;top:176px;font-size:10px;color:#666;text-transform:uppercase}
.blog-title{position:absolute;left:22px;top:198px;width:235px;font-size:13px;font-weight:600;line-height:19px;color:#222}
.blog-text{position:absolute;left:22px;top:244px;width:235px;font-size:11.5px;line-height:18px;color:#666}
.carousel-arrow{top:3238px;width:32px;height:32px;border-radius:50%;border:1.6px solid}
.carousel-arrow svg{position:absolute;left:8px;top:8px}
/* contact */
.contact-band{top:3508px;left:0;width:1200px;height:560px;background:var(--light)}
.contact-panel{left:150px;top:3590px;width:427px;height:355px;background:linear-gradient(135deg,#1c7cc4,#0f5d99)}
.contact-panel h2{position:absolute;left:58px;top:106px;color:#fff;font-family:"Poppins",sans-serif;font-weight:500;font-size:31px}
.contact-panel .rule{position:absolute;left:58px;top:148px;width:40px;height:3px;background:#fff}
.contact-panel p{position:absolute;left:58px;top:166px;width:200px;color:#e6f1fa;font-size:13px;line-height:22px}
.form-card{left:479px;top:3632px;width:569px;height:435px;background:#fff;box-shadow:0 10px 30px rgba(0,0,0,.1)}
.form-card h3{position:absolute;left:50px;top:48px;font-family:"Poppins",sans-serif;font-weight:400;font-size:28px;color:#222}
.form-card h3 b{font-weight:600}
.field{position:absolute;width:206px}
.field label{display:block;font-family:"Poppins",sans-serif;font-size:10px;font-weight:500;color:#222;text-transform:uppercase}
.field span{display:block;margin-top:10px;padding-bottom:10px;font-size:11.5px;color:#9aa0a8;border-bottom:1px solid var(--line)}
.send-btn{left:934px;top:3962px;width:60px;height:60px;border-radius:50%;background:var(--blue);box-shadow:0 6px 16px rgba(21,136,214,.35)}
.send-btn svg{position:absolute;left:17px;top:17px}
/* footer */
.footer-bg{top:4100px;left:0}
.site-footer .brand{position:absolute;left:0;width:1200px;justify-content:center;top:4222px;font-size:28px;color:var(--blue)}
.footer-nav{top:4313px;left:0;width:1200px;display:flex;justify-content:center;gap:26px;font-size:12.5px;color:#b9bec6}
.copyright{left:173px;top:4398px;font-size:12px;color:#b9bec6}
.social{top:4390px;left:524px;display:flex;gap:4px}
.social span{width:32px;height:32px;border-radius:50%;background:var(--blue)}
.legal{top:4398px;right:178px;font-size:12px;color:#b9bec6}
</style>
</head>
<body>

<header class="abs site-header">
  <div class="brand"><span class="brand-mark"></span>Vantrel Works</div>
  <nav class="main-nav">
    <a class="active">Home</a><a>About</a><a>Services</a><a>Partners</a><a>Blog</a><a>Resources ▾</a><a>Contact Us</a>
  </nav>
</header>

<!-- hero -->
<svg class="abs hero-bg" width="1200" height="790" viewBox="0 0 1200 790">
  <defs>
    <linearGradient id="heroGrad" x1="0" y1="0" x2="1" y2="1">
      <stop offset="0" stop-color="#0d2236"/>
      <stop offset=".6" stop-color="#0b1a2c"/>
      <stop offset="1" stop-color="#0a2b4f"/>
    </linearGradient>
    <radialGradient id="globeGrad" cx=".5" cy=".5" r=".5">
      <stop offset="0" stop-color="#3aa6f0"/>
      <stop offset=".55" stop-color="#135ea8" stop-opacity=".8"/>
      <stop offset="1" stop-color="#0b2a4a" stop-opacity="0"/>
    </radialGradient>
    <linearGradient id="waveGrad" x1="0" y1="0" x2="0" y2="1">
      <stop offset="0" stop-color="#eef1f5"/>
      <stop offset="1" stop-color="#ffffff"/>
    </linearGradient>
  </defs>
  <path d="M0 0H1200V621Q900 682 600 778Q300 682 0 629Z" fill="url(#heroGrad)" role="img" aria-label="Night city skyline with a glowing network globe"/>
  <circle cx="821" cy="324" r="300" fill="url(#globeGrad)" role="img" aria-label="Glowing digital globe linked by security shields"/>
  <path d="M0 629Q300 682 600 778Q900 682 1200 621V790H0Z" fill="url(#waveGrad)"/>
  <path d="M330 706Q470 745 600 778Q730 745 870 706" fill="none" stroke="#1588d6" stroke-width="4"/>
</svg>
<p class="abs hero-eyebrow">The Right People For Your Team.</p>
<h1 class="abs hero-title">Cyber Thrieats <span>and</span><br>Digitalisation Risks</h1>
<a class="abs btn btn-primary" style="left:150px;top:498px;width:133px;height:42px">Get Started</a>
<a class="abs btn btn-light" style="left:299px;top:498px;width:132px;height:42px">Learn More</a>
<div class="abs scroll-mouse"></div>

<!-- about -->
<p class="abs eyebrow-blue" style="left:150px;top:960px">About Us</p>
<h2 class="abs about-title">Lorem Ipsum is simply dummy<br>text of the printing</h2>
<p class="abs about-text">Lorem Ipsum is simply dummy text of the printing and typesetting industry. Lorem Ipsum has been the industry's standard dummy text ever since the 1500s, when an unknown printer took a galley of type and scrambled it to make a type specimen book. It has survived not only five centuries, but also the leap into electronic typesetting, remaining essentially unchanged.</p>
<a class="abs btn btn-primary" style="left:150px;top:1253px;width:159px;height:38px">More About Us</a>
<svg class="abs" style="left:655px;top:952px" width="393" height="349" viewBox="0 0 393 349">
  <defs>
    <linearGradient id="aboutGrad" x1="0" y1="0" x2="1" y2="1">
      <stop offset="0" stop-color="#2c3e57"/>
      <stop offset=".5" stop-color="#1b5d97"/>
      <stop offset="1" stop-color="#9aa3ad"/>
    </linearGradient>
  </defs>
  <path d="M60 30Q200 -20 380 30Q395 180 300 280Q240 330 160 349Q40 300 8 150Q30 80 60 30Z" fill="url(#aboutGrad)" role="img" aria-label="Business people using a digital security interface, set in a shield frame"/>
  <path d="M100 60Q230 30 330 70Q330 200 250 280Q200 310 165 320Q80 240 80 140Z" fill="none" stroke="#1e9be6" stroke-width="4"/>
</svg>

<!-- services -->
<svg class="abs" style="left:0;top:1389px" width="1200" height="1244" viewBox="0 0 1200 1244">
  <defs>
    <linearGradient id="svcGrad" x1="0" y1="0" x2="0" y2="1">
      <stop offset="0" stop-color="#142338"/>
      <stop offset="1" stop-color="#1b222d"/>
    </linearGradient>
  </defs>
  <path d="M0 96Q600 -96 1200 96V1244H0Z" fill="url(#svcGrad)"/>
</svg>
<h2 class="abs section-title" style="top:1486px;color:#fff">What <b>We Provide</b></h2>
<div class="abs title-rule" style="top:1543px"></div>
<p class="abs services-intro">Lorem Ipsum is simply dummy text of the printing and typesetting industry. Lorem<br>Ipsum has been the industry's standard dummy text .</p>

<svg width="0" height="0" style="position:absolute">
  <defs>
    <linearGradient id="cardGrad" x1="0" y1="0" x2="0" y2="1">
      <stop offset="0" stop-color="#2c3747"/>
      <stop offset="1" stop-color="#1e2734"/>
    </linearGradient>
    <linearGradient id="cardActive" x1="0" y1="0" x2="0" y2="1">
      <stop offset="0" stop-color="#1f6fb1"/>
      <stop offset="1" stop-color="#0d3a66"/>
    </linearGradient>
    <symbol id="shield" viewBox="0 0 283 267"><path d="M0 42Q0 18 30 10Q141 -12 253 10Q283 18 283 42V120Q283 200 141 267Q0 200 0 120Z"/></symbol>
    <symbol id="teamIcon" viewBox="0 0 62 64"><g fill="none" stroke="#fff" stroke-width="2"><circle cx="31" cy="10" r="8"/><path d="M31 18V26M12 26H50M12 26V34M31 26V34M50 26V34"/><circle cx="12" cy="40" r="5"/><circle cx="31" cy="40" r="5"/><circle cx="50" cy="40" r="5"/><path d="M4 60Q4 48 12 48Q20 48 20 60ZM23 60Q23 48 31 48Q39 48 39 60ZM42 60Q42 48 50 48Q58 48 58 60Z"/></g></symbol>
    <symbol id="chev" viewBox="0 0 16 16"><path d="M6 3L11 8L6 13" fill="none" stroke="#fff" stroke-width="1.8"/></symbol>
  </defs>
</svg>

<div class="abs service-card" style="left:150px;top:1651px"><svg class="shape" width="283" height="267"><use href="#shield" fill="url(#cardGrad)"/></svg><svg class="service-icon" width="62" height="64"><use href="#teamIcon"/></svg><div class="service-sep"></div><p class="service-name">IT<br>Consulting</p><div class="service-go"><svg width="16" height="16"><use href="#chev"/></svg></div></div>
<div class="abs service-card" style="left:458px;top:1651px"><svg class="shape" width="283" height="267"><use href="#shield" fill="url(#cardActive)"/></svg><svg class="service-icon" width="62" height="64"><use href="#teamIcon"/></svg><div class="service-sep"></div><p class="service-name">Vulnerability<br>Assessment</p><div class="service-go"><svg width="16" height="16"><use href="#chev"/></svg></div></div>
<div class="abs service-card" style="left:765px;top:1651px"><svg class="shape" width="283" height="267"><use href="#shield" fill="url(#cardGrad)"/></svg><svg class="service-icon" width="62" height="64"><use href="#teamIcon"/></svg><div class="service-sep"></div><p class="service-name">Information Systems<br>Security Audit</p><div class="service-go"><svg width="16" height="16"><use href="#chev"/></svg></div></div>

<div class="abs service-card" style="left:150px;top:1951px"><svg class="shape" width="283" height="267"><use href="#shield" fill="url(#cardGrad)"/></svg><svg class="service-icon" width="62" height="64"><use href="#teamIcon"/></svg><div class="service-sep"></div><p class="service-name">ISO<br>Compliance</p><div class="service-go"><svg width="16" height="16"><use href="#chev"/></svg></div></div>
<div class="abs service-card" style="left:458px;top:1951px"><svg class="shape" width="283" height="267"><use href="#shield" fill="url(#cardGrad)"/></svg><svg class="service-icon" width="62" height="64"><use href="#teamIcon"/></svg><div class="service-sep"></div><p class="service-name">Penetration<br>Testing</p><div class="service-go"><svg width="16" height="16"><use href="#chev"/></svg></div></div>
<div class="abs service-card" style="left:765px;top:1951px"><svg class="shape" width="283" height="267"><use href="#shield" fill="url(#cardGrad)"/></svg><svg class="service-icon" width="62" height="64"><use href="#teamIcon"/></svg><div class="service-sep"></div><p class="service-name">Security<br>Awareness Training</p><div class="service-go"><svg width="16" height="16"><use href="#chev"/></svg></div></div>

<div class="abs service-card" style="left:150px;top:2250px"><svg class="shape" width="283" height="267"><use href="#shield" fill="url(#cardGrad)"/></svg><svg class="service-icon" width="62" height="64"><use href="#teamIcon"/></svg><div class="service-sep"></div><p class="service-name">Social<br>Engineering Test</p><div class="service-go"><svg width="16" height="16"><use href="#chev"/></svg></div></div>
<div class="abs service-card" style="left:458px;top:2250px"><svg class="shape" width="283" height="267"><use href="#shield" fill="url(#cardGrad)"/></svg><svg class="service-icon" width="62" height="64"><use href="#teamIcon"/></svg><div class="service-sep"></div><p class="service-name">Protection<br>Against DDoS</p><div class="service-go"><svg width="16" height="16"><use href="#chev"/></svg></div></div>
<div class="abs service-card" style="left:765px;top:2250px"><svg class="shape" width="283" height="267"><use href="#shield" fill="url(#cardGrad)"/></svg><svg class="service-icon" width="62" height="64"><use href="#teamIcon"/></svg><div class="service-sep"></div><p class="service-name">Procurement<br>Services</p><div class="service-go"><svg width="16" height="16"><use href="#chev"/></svg></div></div>

<!-- partners -->
<h2 class="abs section-title" style="top:2705px;color:#222">Our <b>Partners</b></h2>
<div class="abs title-rule" style="top:2761px"></div>
<div class="abs partner-featured"></div>
<div class="abs partner" style="left:150px"><i></i>Nordvale</div>
<div class="abs partner" style="left:328px">Kestrix</div>
<div class="abs partner" style="left:522px"><i></i>Harbrook</div>
<div class="abs partner" style="left:716px"><i></i>Quillon</div>
<div class="abs partner" style="left:908px"><i></i>Harbrook</div>
<div class="abs pager"><span></span><span class="on"></span><span></span></div>

<!-- blog -->
<h2 class="abs section-title" style="top:2992px;color:#222">Latest <b>Blog</b></h2>
<div class="abs title-rule" style="top:3048px"></div>
<div class="abs carousel-arrow" style="left:96px;border-color:#9aa0a8"><svg width="16" height="16"><path d="M10 3L5 8L10 13" fill="none" stroke="#9aa0a8" stroke-width="1.8"/></svg></div>
<div class="abs carousel-arrow" style="left:1072px;border-color:var(--blue)"><svg width="16" height="16"><path d="M6 3L11 8L6 13" fill="none" stroke="#1588d6" stroke-width="1.8"/></svg></div>

<article class="abs blog-card" style="left:150px">
  <div class="blog-media" role="img" aria-label="Glowing cloud security symbol over a digital world map" style="background:linear-gradient(135deg,#0a2548,#1670c0 60%,#0b2a52)"></div>
  <div class="blog-more"><svg width="15" height="15"><path d="M2 7.5H13M8 3L13 7.5L8 12" fill="none" stroke="#fff" stroke-width="1.6"/></svg></div>
  <p class="blog-date">Aug 26, 2021</p>
  <h3 class="blog-title">Lorem Ipsum is simply dummy text of the printing industry.</h3>
  <p class="blog-text">Lorem Ipsum is simply dummy text of the printing and typesetting industry. Lorem Ipsum has been the industry's standard dummy text.</p>
</article>
<article class="abs blog-card raised" style="left:461px">
  <div class="blog-media" role="img" aria-label="Hands typing on a laptop with glowing data overlay" style="background:linear-gradient(135deg,#c9ccd0,#8d8670 50%,#2d3a4a)"></div>
  <div class="blog-more"><svg width="15" height="15"><path d="M2 7.5H13M8 3L13 7.5L8 12" fill="none" stroke="#fff" stroke-width="1.6"/></svg></div>
  <p class="blog-date">Aug 26, 2021</p>
  <h3 class="blog-title">Lorem Ipsum is simply dummy text of the printing industry.</h3>
  <p class="blog-text">Lorem Ipsum is simply dummy text of the printing and typesetting industry. Lorem Ipsum has been the industry's standard dummy text.</p>
</article>
<article class="abs blog-card" style="left:772px">
  <div class="blog-media" role="img" aria-label="Digital padlock above a keyboard in blue light" style="background:linear-gradient(135deg,#0c2f3f,#15889a 55%,#0a2638)"></div>
  <div class="blog-more"><svg width="15" height="15"><path d="M2 7.5H13M8 3L13 7.5L8 12" fill="none" stroke="#fff" stroke-width="1.6"/></svg></div>
  <p class="blog-date">Aug 26, 2021</p>
  <h3 class="blog-title">Lorem Ipsum is simply dummy text of the printing industry.</h3>
  <p class="blog-text">Lorem Ipsum is simply dummy text of the printing and typesetting industry. Lorem Ipsum has been the industry's standard dummy text.</p>
</article>

<!-- contact -->
<div class="abs contact-band"></div>
<div class="abs contact-panel" role="img" aria-label="Team at work in an office, tinted blue">
  <h2>CONTACT US</h2><div class="rule"></div>
  <p>Lorem Ipsum is simply dummy text of the printing and typesetting industry. Lorem Ipsum has been the industry.</p>
</div>
<form class="abs form-card">
  <h3>GET IN <b>TOUCH</b></h3>
  <div class="field" style="left:54px;top:120px"><label>Your Name</label><span>Jonathan</span></div>
  <div class="field" style="left:309px;top:120px"><label>Company Name</label><span>Company Name</span></div>
  <div class="field" style="left:54px;top:193px"><label>Email Address*</label><span>jonathan.smith@inbox.example</span></div>
  <div class="field" style="left:309px;top:193px"><label>Phone*</label><span>123-456-7890</span></div>
  <div class="field" style="left:54px;top:266px;width:400px"><label>Message</label><span style="padding-bottom:56px">Hi, do you have a moment to talk abo...|</span></div>
</form>
<div class="abs send-btn"><svg width="26" height="26" viewBox="0 0 26 26"><path d="M2 12L24 3L17 24L12 15Z" fill="#fff"/><path d="M12 15L24 3" stroke="#1588d6" stroke-width="1.5"/></svg></div>

<!-- footer -->
<svg class="abs footer-bg" width="1200" height="401" viewBox="0 0 1200 401">
  <path d="M0 180Q600 -116 1200 180V401H0Z" fill="#242527"/>
  <path d="M380 86Q490 48 600 30Q710 48 820 86" fill="none" stroke="#1588d6" stroke-width="4"/>
</svg>
<footer class="site-footer">
  <div class="brand"><span class="brand-mark"></span>Vantrel Works</div>
  <nav class="abs footer-nav"><span>Home</span><span>About</span><span>Services</span><span>Partners</span><span>Blog</span><span>Resources</span><span>Contact Us</span></nav>
  <p class="abs copyright">© 2021 Vantrelworks. All Rights Reserved.</p>
  <div class="abs social"><span aria-label="Social link"></span><span aria-label="Social link"></span><span aria-label="Social link"></span><span aria-label="Social link"></span></div>
  <p class="abs legal">Privacy Policy &nbsp;|&nbsp; Terms of Use</p>
</footer>

</body>
</html>
```